Website Design for Venture Capital firm

Create website for venture capital firm. Website Instructions
Use https://www.korventholdings.com/ as a reference website.
Use images of Downtown Austin, Texas.
Use images of business executives in business suits, pictures of money coins stacked like a graph cart.
Use images of downtown high rise buildings.
Use the same image of the Big Ben Clock that appears on Korvent Holdings website.
Use images associated with Venture Technology Incubator.
Use images associated with Venture Angel Investor.
Create Section Heads for the menu bar for each of the sections below.
Use the Orchid Slate Advisors HEADER to guide your style
Target Market(s)
Venture Capital Investors
Number of Pages Required
1 page
Look and feel
Each slider illustrates characteristics of the customer's brand and the style your logo design should communicate.

```html
<!DOCTYPE html>
<html lang="en">
<head>
<meta charset="utf-8">
<title>Orchid Slate Advisors</title>
<link rel="stylesheet" href="https://fonts.googleapis.com/css2?family=Jost:wght@400;500&family=Nunito:wght@400;600;700&display=swap">
<style>
:root{
  --gold:#a8962a;
  --sage:#9bb0a0;
  --ink:#2b2b2b;
  --text:#6d6d6d;
  --white:#ffffff;
  --navy:#0f2f6a;
  --rule:#cfcfcf;
}
*{margin:0;padding:0;box-sizing:border-box}
html,body{width:1200px;height:3524px;overflow:hidden;background:var(--white)}
body{position:relative;font-family:'Nunito',sans-serif;color:var(--text)}
.abs{position:absolute}
.btn{position:absolute;display:flex;align-items:center;justify-content:center;border-radius:22px;font-family:'Nunito',sans-serif;font-weight:600;font-size:15px;color:var(--white);text-decoration:none}
.btn-gold{background:var(--gold)}
.btn-sage{background:var(--sage)}
.heading{font-family:'Jost',sans-serif;font-weight:500;color:var(--ink);text-transform:uppercase;letter-spacing:.5px;font-size:36px;line-height:52px}
.body-copy{font-size:15.5px;line-height:29px}

/* Hero */
.hero{left:0;top:0;width:1200px;height:576px;background:linear-gradient(180deg,#13277a 0%,#1d3a8e 35%,#3b4a6e 65%,#8a5a3a 82%,#1a2a3a 100%)}
.brand{left:112px;top:38px;color:var(--white);font-family:'Jost',sans-serif;font-weight:500;font-size:24px;letter-spacing:2px;line-height:28px;text-align:center}
.brand small{display:block;font-size:11px;letter-spacing:6px;line-height:14px}
.main-nav{left:425px;top:46px;display:flex;gap:32px;font-size:14px;color:var(--white)}
.main-nav .active{color:var(--gold);border-bottom:2px solid var(--gold);padding-bottom:10px}
.hero-title{left:0;width:1200px;top:168px;text-align:center;font-family:'Jost',sans-serif;font-weight:500;font-size:56px;line-height:69px;color:var(--white);text-transform:uppercase}
.hero-sub{left:270px;width:660px;top:320px;text-align:center;font-size:18px;line-height:33px;color:var(--white)}
.notch{left:540px;top:548px}

/* About */
.about-block{left:59px;top:668px;width:300px;height:306px;border-radius:44px;background:var(--sage)}
.about-photo{left:111px;top:717px;width:488px;height:479px;border-radius:44px;background:linear-gradient(135deg,#c8b89a 0%,#6b6a6a 45%,#2d3540 100%);opacity:.95}

/* Incubator */
.incubator{left:0;top:1320px;width:1200px;height:557px;background:linear-gradient(100deg,#e4ecf9 0%,#c3d6f2 45%,#7f9fd0 70%,#3f5f96 100%)}

/* Benefits */
.benefit-icon{left:694px;width:70px;height:70px;border-radius:50%;background:var(--gold)}
.benefit-text{left:694px;width:392px;font-size:15.5px;line-height:32px}
.benefit-rule{left:694px;width:395px;height:1px;background:var(--rule)}

/* Risks */
.risks{left:0;top:2729px;width:1200px;height:558px;background:radial-gradient(ellipse at 60% 40%,#1f5aa8 0%,#0e3a7a 55%,#0a2758 100%)}
.tower-photo{left:0;top:2729px;width:300px;height:558px;background:linear-gradient(90deg,rgba(120,70,30,.55) 0%,rgba(160,90,35,.45) 55%,rgba(14,58,122,0) 100%)}

/* Footer */
.foot-brand{left:0;width:1200px;top:3326px;text-align:center;color:var(--sage);font-family:'Jost',sans-serif;font-weight:500;font-size:26px;letter-spacing:3px;line-height:30px}
.foot-brand small{display:block;font-size:10px;letter-spacing:8px;line-height:12px}
.foot-nav{left:0;width:1200px;top:3391px;display:flex;justify-content:center;gap:38px;font-size:16px;color:#444}
.foot-nav .active{color:#111}
.social{top:3434px;width:30px;height:30px;border-radius:50%;background:var(--gold)}
.copyright{left:0;width:1200px;top:3482px;text-align:center;font-size:13px;color:#555}
.bottom-rule{left:0;top:3519px;width:1200px;height:5px;background:#bdbdbd}
</style>
</head>
<body>

<header>
  <div class="abs hero" role="img" aria-label="Downtown Austin skyline at dusk with river and lit towers"></div>
  <div class="abs brand">ORCHID SLATE<small>ADVISORS</small></div>
  <nav class="abs main-nav">
    <span class="active">Home</span><span>About Us</span><span>Investment Model</span><span>Investor Network</span><span>Benefits</span>
  </nav>
  <a class="btn btn-gold" style="left:951px;top:36px;width:137px;height:42px">Contact Us</a>
  <h1 class="abs hero-title">Empowering You<br>With Insightful Solutions</h1>
  <p class="abs hero-sub">Orchid Slate Advisors typically invests $50,000 to $100,000 of seed capital to incubate each of its portfolio companies.</p>
  <a class="btn btn-gold" style="left:450px;top:404px;width:138px;height:42px">Get Started</a>
  <a class="btn btn-sage" style="left:613px;top:404px;width:137px;height:42px">Join With Us</a>
  <svg class="abs notch" width="120" height="28" viewBox="0 0 120 28">
    <path d="M0 28 C20 28 25 0 60 0 C95 0 100 28 120 28Z" fill="#fff"/>
    <rect x="49" y="8" width="22" height="34" rx="11" fill="#9a9a9a"/>
    <path d="M60 12 V24 M55 20 L60 25 L65 20" stroke="#fff" stroke-width="1.6" fill="none"/>
  </svg>
</header>

<section class="about">
  <div class="abs about-block"></div>
  <div class="abs about-photo" role="img" aria-label="Two business executives in suits reviewing documents"></div>
  <h2 class="abs heading" style="left:676px;top:734px">About Us</h2>
  <div class="abs body-copy" style="left:676px;top:796px;width:410px">
    <p>Similar to other leading technology incubators, Orchid Slate Advisors provides a combination of seed capital investment, infrastructure resources and Harbor Strategy Group-level strategic guidance so that our incubated companies can gain momentum right from the first day of launch.</p>
    <p style="margin-top:17px">Incubator venture firms like BrightForge Labs and Keystone Accelerator have incubated companies that grew to become some of the leading corporations in the US including Nestway, Curbside Eats and Pantrypal.</p>
  </div>
  <a class="btn btn-sage" style="left:676px;top:1124px;width:137px;height:43px">Read More</a>
</section>

<section class="incubator-section">
  <div class="abs incubator" role="img" aria-label="Glass high-rise towers seen from below against a pale sky"></div>
  <h2 class="abs heading" style="left:108px;top:1460px">Incubator and Seed Stage<br>Investment Model</h2>
  <p class="abs body-copy" style="left:111px;top:1574px;width:400px">Orchid Slate Advisors typically invests $50,000 to $100,000 of seed capital to incubate each of its portfolio companies.</p>
  <a class="btn btn-sage" style="left:111px;top:1683px;width:137px;height:42px">Read More</a>
</section>

<section class="benefits">
  <h2 class="abs heading" style="left:111px;top:1959px">Benefits of Investing in<br>Venture</h2>
  <p class="abs body-copy" style="left:111px;top:2073px;width:515px;line-height:32px">Venture capital allows investors to diversify their portfolios beyond traditional asset classes (stocks, bonds, real estate). Investing in venture capital deals can lead to significant returns, especially if the company grows rapidly or goes public.</p>
  <a class="btn btn-sage" style="left:111px;top:2220px;width:137px;height:43px">Read More</a>

  <div class="abs benefit-icon" style="top:1971px"></div>
  <svg class="abs" style="left:694px;top:1971px" width="70" height="70" viewBox="0 0 70 70" fill="none" stroke="#fff" stroke-width="1.6"><circle cx="35" cy="33" r="12"/><path d="M30 33h10M35 28v10"/><path d="M24 48h22"/></svg>
  <p class="abs benefit-text" style="top:2061px">Early-stage investments in successful startups often yield returns much higher than traditional investments like stocks or bonds.</p>
  <div class="abs benefit-rule" style="top:2179px"></div>

  <div class="abs benefit-icon" style="top:2217px"></div>
  <svg class="abs" style="left:694px;top:2217px" width="70" height="70" viewBox="0 0 70 70" fill="none" stroke="#fff" stroke-width="1.8"><circle cx="35" cy="35" r="17"/><circle cx="35" cy="35" r="12"/><path d="M29 35l4 4 8-8"/></svg>
  <p class="abs benefit-text" style="top:2307px">Many successful startups are acquired by larger companies or go public through an IPO (Initial Public Offering).</p>
  <div class="abs benefit-rule" style="top:2425px"></div>

  <div class="abs benefit-icon" style="top:2463px"></div>
  <svg class="abs" style="left:694px;top:2463px" width="70" height="70" viewBox="0 0 70 70" fill="none" stroke="#fff" stroke-width="1.8"><path d="M46 22c-8 0-16 6-20 14l8 8c8-4 14-12 14-20z"/><path d="M28 40l-6 8M32 44l-4 6"/><circle cx="40" cy="30" r="3"/></svg>
  <p class="abs benefit-text" style="top:2553px">Successful venture investments can compound over time, creating a strong foundation for long-term wealth creation.</p>
  <div class="abs benefit-rule" style="top:2671px"></div>
</section>

<section class="risks-section">
  <div class="abs risks" role="img" aria-label="Deep blue night sky"></div>
  <div class="abs tower-photo" role="img" aria-label="Photo of an illuminated clock tower at night"></div>
  <h2 class="abs heading" style="left:420px;top:2929px;color:var(--white)">Risks of Investing as an Angel<br>Venture Investor</h2>
  <p class="abs body-copy" style="left:420px;top:3043px;width:670px;color:var(--white)">Startups often need to raise multiple rounds of funding to grow. As new investors come in, early investors' ownership percentage can be diluted. If the company raises additional capital at a lower valuation, this could further erode an investor's share.</p>
  <a class="btn btn-sage" style="left:420px;top:3157px;width:137px;height:43px">Read More</a>
</section>

<footer>
  <div class="abs foot-brand">ORCHID SLATE<small>ADVISORS</small></div>
  <nav class="abs foot-nav">
    <span class="active">Home</span><span>About Us</span><span>Investment Model</span><span>Investor Network</span><span>Benefits</span><span>Contact Us</span>
  </nav>
  <div class="abs social" style="left:548px"></div>
  <div class="abs social" style="left:585px"></div>
  <div class="abs social" style="left:622px"></div>
  <p class="abs copyright">(C) Copyright 2024 | All Rights Reserved</p>
  <div class="abs bottom-rule"></div>
</footer>

</body>
</html>
```